Business Card Design Project

we need a business card design for our company: www.plomvik.ch
It's important to include our already existing logo (see website)

```html
<!DOCTYPE html>
<html lang="en">
<head>
<meta charset="utf-8">
<title>Plomvik Business Card</title>
<link rel="stylesheet" href="https://fonts.googleapis.com/css2?family=Saira+Semi+Condensed:wght@400;600&display=swap">
<style>
  :root {
    --page: #ffffff;
    --card-dark: #0a0a0a;
    --card-light: #ffffff;
    --brand-blue: #3b55f0;
    --accent-deep: #3a2fb0;
    --accent-cyan: #19e6ff;
    --tagline: #2f7cf5;
    --url-dark: #e8ecff;
    --url-light: #2536b0;
  }
  * { box-sizing: border-box; margin: 0; padding: 0; }
  html, body {
    width: 1200px;
    height: 813px;
    overflow: hidden;
    background: var(--page);
  }
  .canvas {
    position: relative;
    width: 1200px;
    height: 813px;
  }
  .card {
    position: absolute;
    width: 564px;
    height: 340px;
    border-radius: 16px;
    overflow: hidden;
    box-shadow: 0 3px 10px rgba(0, 0, 0, 0.25);
  }
  .card--back { left: 44px; top: 40px; background: var(--card-dark); }
  .card--front { left: 576px; top: 430px; background: var(--card-light); }
  .card__accent {
    position: absolute;
    left: 0;
    top: 0;
    width: 90px;
    height: 100%;
    background: linear-gradient(180deg, var(--accent-deep) 0%, var(--brand-blue) 50%, var(--accent-cyan) 100%);
  }
  .card__identity {
    position: absolute;
    left: 0;
    width: 100%;
    padding-left: 70px;
    text-align: center;
    font-family: "Saira Semi Condensed", sans-serif;
  }
  .card--back .card__identity { top: 100px; }
  .card--front .card__identity { top: 92px; }
  .brand-name {
    display: inline-flex;
    align-items: center;
    gap: 12px;
    font-size: 84px;
    font-weight: 600;
    line-height: 1;
    color: var(--brand-blue);
  }
  .brand-name__mark {
    width: 30px;
    height: 30px;
    background: var(--brand-blue);
  }
  .tagline {
    margin-top: 8px;
    font-size: 17px;
    font-weight: 400;
    line-height: 1.1;
    letter-spacing: 0.3px;
    color: var(--tagline);
  }
  .web {
    font-size: 17px;
    font-weight: 400;
    line-height: 1.1;
  }
  .card--back .web { color: var(--url-dark); }
  .card--front .web { color: var(--url-light); }
</style>
</head>
<body>
<main class="canvas">

  <section class="card card--back" aria-label="Card back">
    <div class="card__accent" role="img" aria-label="Blue to cyan decorative accent"></div>
    <div class="card__identity">
      <div class="brand-name"><span class="brand-name__mark"></span>Plomvik</div>
      <p class="tagline">PLOMVIK SOFTWARE GROUP</p>
      <p class="web">www.plomvik.ch</p>
    </div>
  </section>

  <section class="card card--front" aria-label="Card front">
    <div class="card__accent" role="img" aria-label="Blue to cyan decorative accent"></div>
    <div class="card__identity">
      <div class="brand-name"><span class="brand-name__mark"></span>Plomvik</div>
      <p class="tagline">PLOMVIK SOFTWARE GROUP</p>
      <p class="web">www.plomvik.ch</p>
    </div>
  </section>

</main>
</body>
</html>
```